Rising Stewards Scheme. Brochure to Inform Target Audience.

Rising Steward Scheme:

4 Page Brochure
Aimed at Parents and Children (Age 11-16)
Programme Overview
Specific Focus on Bronze Award with Learning Objectives and Enabling Objectives from Content Document
Contact Area Needed
How to Book - Online through the Website
Should encourage people to want to join it or sign up

you can use stock rugby images if needed

Target Market(s)

children between ages 11-16 and parents, gatekeepers (schools, rugby clubs)

Industry/Entity Type

Education

Font styles to use
Serif
Sans Serif

Requirements
Must have
• the programme content, each award continent and bronze award learning objectives
• Colours should match existing work that has been created
• Get in touch: www.valemark-rss.com
• maris@valemark-rss.com
Nice to have
• graphics of kids playing rugby if possible from stock images

```html
<!DOCTYPE html>
<html lang="en">
<head>
<meta charset="utf-8">
<title>Rising Stewards Scheme – Brochure</title>
<link href="https://fonts.googleapis.com/css2?family=Raleway:ital,wght@0,400;0,600;0,700;0,800;0,900;1,400&display=swap" rel="stylesheet">
<style>
:root{
  --yellow:#f5b400;
  --ink:#222222;
  --charcoal:#2b2b2b;
  --slate:#3d3d3d;
  --mist:#eeeeee;
  --paper:#ffffff;
  --stage:#e9e7e3;
  --grass:#4f7d2c;
  --bronze:#b06a38;
  --silver:#b9bcc0;
  --gold:#d8a520;
}
*{box-sizing:border-box;margin:0;padding:0}
html,body{width:1200px;height:749px;overflow:hidden;background:var(--stage)}
body{font-family:"Raleway",Arial,sans-serif;color:var(--ink)}
.canvas{position:relative;width:1200px;height:749px;overflow:hidden;background:var(--stage)}
.page{position:absolute;width:260px;height:368px;overflow:hidden;box-shadow:0 6px 18px rgba(0,0,0,.18)}
.spread{position:absolute;left:32px;top:190px;width:520px;height:368px;display:flex;box-shadow:0 6px 18px rgba(0,0,0,.18)}
.spread .page{position:relative;box-shadow:none}

/* ---------- Programme overview page ---------- */
.overview{background:var(--paper);display:flex;flex-direction:column}
.overview-header{height:18px;background:var(--yellow);color:var(--paper);font-weight:800;font-size:9px;padding:4px 10px}
.overview-intro{font-size:3.7px;line-height:1.35;padding:3px 10px 3px;color:var(--slate)}
.overview-intro b{color:var(--ink)}
.award-list{display:flex;flex-direction:column;gap:2px;padding:0 10px}
.award{display:grid;grid-template-columns:26px 1fr;gap:5px;min-height:36px}
.award-medal{background:var(--mist);display:flex;align-items:center;justify-content:center}
.award-medal span{width:18px;height:18px;border-radius:50%;display:block}
.medal-bronze{background:radial-gradient(circle at 35% 35%,#e3a06d,var(--bronze))}
.medal-silver{background:radial-gradient(circle at 35% 35%,#eef0f2,var(--silver))}
.medal-gold{background:radial-gradient(circle at 35% 35%,#f7dc80,var(--gold))}
.award h3{font-size:5px;font-weight:800;margin:1px 0 1px}
.award p{font-size:3.5px;line-height:1.3;color:var(--slate)}
.values{padding:4px 10px 2px}
.values h2{font-size:8px;font-weight:800;color:var(--yellow);margin-bottom:2px}
.value{display:grid;grid-template-columns:7px 1fr;gap:3px;align-items:start;margin-bottom:2.4px;font-size:3.7px;line-height:1.3;color:var(--slate)}
.value svg{width:6px;height:6px}
.value b{color:var(--yellow);font-weight:800}
.events{background:var(--charcoal);color:var(--paper);padding:4px 10px 4px;margin-top:auto}
.events h2{font-size:8px;font-weight:800;color:var(--yellow)}
.events-note{font-style:italic;font-size:3.6px;line-height:1.3;margin:1px 0 2px}
.event{font-size:3.8px;line-height:1.55;display:flex;gap:3px;align-items:center}
.event::before{content:"";border-left:3px solid var(--yellow);border-top:1.8px solid transparent;border-bottom:1.8px solid transparent}
.event b{color:var(--yellow);font-weight:800}
.team-photo{height:58px;flex:none;background:linear-gradient(90deg,#6a5a2a 0%,#c9a23a 18%,#4b4b3f 34%,#7f8b55 50%,#3e3a2c 66%,#b88f2c 82%,#56603a 100%)}

/* ---------- Bronze teaching page ---------- */
.teaching{background:linear-gradient(180deg,#262826 0%,#2e332c 55%,#3c5a27 80%,var(--grass) 100%)}
.teaching-title{position:absolute;left:10px;top:9px;font-size:10.5px;font-weight:700;color:var(--paper)}
.teaching-title b{color:var(--yellow);font-weight:900}
.teach-table{position:absolute;left:10px;top:30px;width:205px;font-size:3.4px;line-height:1.3}
.teach-head{display:grid;grid-template-columns:44px 48px 1fr;height:12px;font-weight:800;font-size:3.6px}
.teach-head span{padding:2px 2px;background:rgba(30,30,30,.9);color:var(--paper)}
.teach-head .col-training{background:var(--yellow);color:var(--ink)}
.teach-head .col-points{color:var(--yellow)}
.objective-group{display:grid;grid-template-columns:44px 1fr;border-top:.6px solid rgba(255,255,255,.35)}
.training-cell{background:rgba(45,45,45,.92);color:var(--paper);font-weight:700;padding:3px 2px;display:flex;align-items:center}
.enabling-row{display:grid;grid-template-columns:48px 1fr;height:15.6px;border-bottom:.5px solid rgba(255,255,255,.22)}
.enabling-cell{background:rgba(25,25,25,.88);color:var(--yellow);font-weight:700;padding:2px 2px;display:flex;align-items:center}
.points{list-style:none;background:rgba(90,90,90,.62);color:var(--paper);padding:2.5px 3px}
.points li{display:flex;gap:2px}
.points li::before{content:"";width:1.6px;height:1.6px;margin-top:1.2px;background:var(--yellow);flex:none}

/* ---------- Cover ---------- */
.cover{left:584px;top:190px}
.cover-scene{position:absolute;inset:0;background:linear-gradient(180deg,#1c1f1b 0%,#2d332a 30%,#3f4a31 48%,#4d7a2b 68%,#5d8f34 100%)}
.brand{position:absolute;left:14px;top:18px;display:flex;flex-direction:column;align-items:flex-start;gap:4px}
.brand-mark{width:24px;height:24px;border-radius:50%;border:1.5px solid var(--yellow)}
.brand-name{font-size:7px;font-weight:700;color:var(--yellow)}
.scheme-name{font-size:7px;font-weight:700;color:var(--yellow);text-transform:uppercase;letter-spacing:.3px;line-height:1.15}
.cover-title{position:absolute;left:100px;top:26px;color:var(--paper);font-weight:600;font-size:14.5px;line-height:1.05;text-transform:uppercase}
.cover-title b{display:block;font-weight:900;font-size:16px}

/* ---------- FAQ / back page ---------- */
.back{left:876px;top:190px;display:flex;flex-direction:column}
.faq{height:210px;background:linear-gradient(180deg,#272827,#2f312e);padding:10px 12px 0}
.faq h2{font-size:14px;font-weight:800;color:var(--yellow);margin-bottom:4px}
.faq-item{margin-bottom:3.2px}
.faq-item h3{font-size:4.2px;font-weight:800;color:var(--yellow);margin-bottom:.6px}
.faq-item p{font-size:3.6px;line-height:1.3;color:var(--paper)}
.mission{height:55px;background:linear-gradient(180deg,#456b27,var(--grass) 60%,#5e913a);padding:10px 12px 0}
.mission h2{font-size:9px;font-weight:800;color:var(--yellow);margin-bottom:2px}
.mission p{font-size:3.8px;font-weight:700;color:var(--paper);text-transform:uppercase;letter-spacing:.2px}
.about{flex:1;background:var(--yellow);padding:7px 12px 0;color:var(--ink)}
.about h2{font-size:10px;font-weight:800;margin-bottom:3px}
.about p{font-size:3.6px;line-height:1.35;margin-bottom:2.6px}
.about .contact{font-weight:700}
</style>
</head>
<body>
<main class="canvas">

  <section class="spread">
    <article class="page overview">
      <header class="overview-header">Programme Overview</header>
      <p class="overview-intro">Valemark have created a programme which enables each individual to maximise their learning potential so that you can be the best you can be. We provide a fun and healthy environment which is supported by highly motivated coaches who provide excellent individual care and attention. The programme is delivered over three Awards: <b>Bronze, Silver and Gold.</b></p>

      <div class="award-list">
        <div class="award">
          <div class="award-medal" role="img" aria-label="Bronze medal"><span class="medal-bronze"></span></div>
          <div>
            <h3>Bronze Award</h3>
            <p>The Bronze Award is focused on the ‘Team’ and is aimed at children between the ages of 11 and 13. During the Award you will improve your self-confidence and independence whilst having the opportunity to lead and inspire others. We will encourage your natural skills and help you identify the areas that you may wish to develop in the future. Each day we will build your skills through both physical and mental challenges both on and off the pitch. The Award is delivered over 5 days. Days 1 and 2 are delivered at Ashcombe Park and days 3 to 5 are delivered at Harbourside RFC.</p>
          </div>
        </div>
        <div class="award">
          <div class="award-medal" role="img" aria-label="Silver medal"><span class="medal-silver"></span></div>
          <div>
            <h3>Silver Award</h3>
            <p>On completion of the Bronze Award you are eligible to enrol on the Silver Award which is focused on the ‘Individual’. This is aimed at 13 to 14 year olds and is delivered over a 5 day period split between Ashcombe Park and Harbourside RFC. During this award we will be empowering you to discover your own strengths and weaknesses in order to find your most natural leadership style so that we build transformative skills for the future.</p>
          </div>
        </div>
        <div class="award">
          <div class="award-medal" role="img" aria-label="Gold medal"><span class="medal-gold"></span></div>
          <div>
            <h3>Gold Award</h3>
            <p>This is a 5 day residential course for all those who have successfully completed the Bronze and Silver Award. Aimed at 14 - 16s it is the culmination of the Valemark Rugby Rising Stewards Scheme. During this award leaders will be challenged with a variety of practical exercises and on-field activities in order to develop a rounded leader. Individuals will learn how to tackle complex problems and plan missions whilst feeling confident that they can lead others. These skills will equip them for their future learning and workplace environments.</p>
          </div>
        </div>
      </div>

      <section class="values">
        <h2>Our Values</h2>
        <div class="value"><svg viewBox="0 0 10 10"><circle cx="5" cy="5" r="4" fill="none" stroke="#f5b400" stroke-width="1.6"/></svg><p><b>Leadership.</b> For the team to be truly successful we believe in developing leadership at all levels.</p></div>
        <div class="value"><svg viewBox="0 0 10 10"><path d="M5 1 9 9H1Z" fill="#f5b400"/></svg><p><b>Courage.</b> We put the needs of the team ahead of the needs of our own.</p></div>
        <div class="value"><svg viewBox="0 0 10 10"><rect x="1.5" y="1.5" width="7" height="7" fill="#f5b400"/></svg><p><b>Selfless Commitment.</b> We have the physical and mental courage to possess confidence, bravery and resolution when faced with danger or fear.</p></div>
        <div class="value"><svg viewBox="0 0 10 10"><path d="M1 6 4 9 9 1" fill="none" stroke="#f5b400" stroke-width="1.8"/></svg><p><b>Resilience.</b> Our strength of character to overcome adversity and bounce back.</p></div>
        <div class="value"><svg viewBox="0 0 10 10"><circle cx="5" cy="5" r="4" fill="#f5b400"/></svg><p><b>Respect.</b> We respect those people who we train with and compete against. We believe in equal treatment and opportunity for all.</p></div>
      </section>

      <section class="events">
        <h2>Events</h2>
        <p class="events-note">The events will be scheduled through Ticketra.com and therefore the API needs to be directed to the Website</p>
        <p class="event"><span><b>Bronze Award Part 1</b> &nbsp;£179 . 22-23 October 2018, Ashcombe Park</span></p>
        <p class="event"><span><b>Bronze Award Part 2</b> &nbsp;£179 . Harbourside RFC 21-23 February 2018</span></p>
        <p class="event"><span><b>Bronze Award Part 1 &amp; 2</b> &nbsp;£299 . 22-23 October and 21-23 February 2018</span></p>
      </section>
      <div class="team-photo" role="img" aria-label="Strip of photos of young players training and playing rugby"></div>
    </article>

    <article class="page teaching" role="img" aria-label="Photo of a young rugby player running with the ball on a pitch">
      <h1 class="teaching-title"><b>What do we Teach</b> at the Bronze Award</h1>
      <div class="teach-table">
        <div class="teach-head"><span class="col-training">Training Objective (Performance)</span><span class="col-enabling">Enabling Objective</span><span class="col-points">Key Learning Points</span></div>

        <div class="objective-group">
          <div class="training-cell">Demonstrate the attributes required to be a successful leader</div>
          <div>
            <div class="enabling-row"><div class="enabling-cell">Discuss the role of leadership</div><ul class="points"><li>Describe why leaders set a clear direction</li><li>Explain how leaders support their team</li></ul></div>
            <div class="enabling-row"><div class="enabling-cell">Describe the skills of a leader</div><ul class="points"><li>List the key skills a good leader uses</li><li>Identify skills you already show every day</li></ul></div>
            <div class="enabling-row"><div class="enabling-cell">Describe what makes a good team leader</div><ul class="points"><li>Explain how good leaders earn trust</li><li>Describe how a leader keeps people together</li></ul></div>
            <div class="enabling-row"><div class="enabling-cell">Describe leadership opportunities</div><ul class="points"><li>Identify chances to lead at school</li><li>Identify chances to lead at your club</li></ul></div>
            <div class="enabling-row"><div class="enabling-cell">Describe what leadership skills you have</div><ul class="points"><li>Reflect on the skills you bring to a team</li><li>Set one goal to grow as a leader</li></ul></div>
          </div>
        </div>

        <div class="objective-group">
          <div class="training-cell">Demonstrate effective communication</div>
          <div>
            <div class="enabling-row"><div class="enabling-cell">Discuss the importance of communication</div><ul class="points"><li>Explain why clear messages help a team</li><li>Describe what happens when it breaks down</li></ul></div>
            <div class="enabling-row"><div class="enabling-cell">Demonstrate verbal and non verbal communication</div><ul class="points"><li>Show how tone and body language work</li><li>Practise giving instructions on the pitch</li></ul></div>
            <div class="enabling-row"><div class="enabling-cell">Describe the key elements of communication</div><ul class="points"><li>Identify sender, message and receiver</li><li>Explain how to check understanding</li></ul></div>
            <div class="enabling-row"><div class="enabling-cell">Describe being a good listener</div><ul class="points"><li>Describe how to listen without interrupting</li><li>Practise repeating back what was said</li></ul></div>
          </div>
        </div>

        <div class="objective-group">
          <div class="training-cell">Demonstrate effective followership</div>
          <div>
            <div class="enabling-row"><div class="enabling-cell">Discuss the role of followership</div><ul class="points"><li>Explain why every leader also follows</li><li>Describe how followers shape a team</li></ul></div>
            <div class="enabling-row"><div class="enabling-cell">Define the term followership</div><ul class="points"><li>Define followership in your own words</li><li>Compare active and passive followers</li></ul></div>
            <div class="enabling-row"><div class="enabling-cell">How followership is applied and vital in influence</div><ul class="points"><li>Explain how followers influence decisions</li><li>Describe loyal and honest support</li></ul></div>
            <div class="enabling-row"><div class="enabling-cell">Discuss the essential qualities of followership</div><ul class="points"><li>List the qualities of a good follower</li><li>Show initiative while supporting the plan</li></ul></div>
          </div>
        </div>

        <div class="objective-group">
          <div class="training-cell">Demonstrate the attributes required to be a Team Player</div>
          <div>
            <div class="enabling-row"><div class="enabling-cell">Discuss the importance of teamwork in achieving a goal</div><ul class="points"><li>Explain how shared goals build a team</li><li>Describe your role within a squad</li></ul></div>
            <div class="enabling-row"><div class="enabling-cell">Discuss the importance of being a team-minded player</div><ul class="points"><li>Describe how to put the team first</li><li>Show how to encourage team mates</li></ul></div>
            <div class="enabling-row"><div class="enabling-cell">Discuss respect for other views and its influence</div><ul class="points"><li>Explain how to value other views</li><li>Describe how respect builds trust</li></ul></div>
            <div class="enabling-row"><div class="enabling-cell">Discuss what selfless commitment is</div><ul class="points"><li>Define selfless commitment simply</li><li>Give examples from rugby and from life</li></ul></div>
          </div>
        </div>

        <div class="objective-group">
          <div class="training-cell">Demonstrate an understanding of the Valemark Rugby Values</div>
          <div>
            <div class="enabling-row"><div class="enabling-cell">Discuss the importance of having courage</div><ul class="points"><li>Describe physical and moral courage</li><li>Explain how courage helps you lead</li></ul></div>
            <div class="enabling-row"><div class="enabling-cell">Discuss what we mean by team resilience</div><ul class="points"><li>Explain how teams bounce back</li><li>Describe ways to keep going under pressure</li></ul></div>
            <div class="enabling-row"><div class="enabling-cell">Discuss what we mean by respect</div><ul class="points"><li>Explain respect for officials and opponents</li><li>Show respect on and off the pitch</li></ul></div>
          </div>
        </div>
      </div>
    </article>
  </section>

  <article class="page cover">
    <div class="cover-scene" role="img" aria-label="Photo of young players in yellow kit behind a rugby ball resting on the grass"></div>
    <div class="brand">
      <span class="brand-mark"></span>
      <span class="brand-name">Valemark Rugby</span>
      <span class="scheme-name">Rising Stewards<br>Scheme</span>
    </div>
    <h1 class="cover-title">Learn to lead<br>and play the<b>Valemark way</b></h1>
  </article>

  <article class="page back">
    <section class="faq">
      <h2>FAQ</h2>
      <div class="faq-item"><h3>Will you provide lunch or snacks?</h3><p>Water will be provided to refill water bottles. However, we ask that children bring their own lunch.</p></div>
      <div class="faq-item"><h3>Who attends your Rising Stewards Scheme?</h3><p>Children of all abilities, some who have played rugby before and some who have never played. The programme is suitable for both boys and girls.</p></div>
      <div class="faq-item"><h3>When do I drop and pick up my child from the programme?</h3><p>Drop off and pick up times are shown on your booking. Please arrive ten minutes early so your child can register.</p></div>
      <div class="faq-item"><h3>What should my child wear?</h3><p>Activities take place both indoor and outdoor. Please dress your child in sports kit, boots and trainers.</p></div>
      <div class="faq-item"><h3>What makes your programme the right choice for my child?</h3><p>The programme is fun and designed to develop the child's leadership skills on and off the pitch.</p></div>
      <div class="faq-item"><h3>How can I enrol on the silver or gold award?</h3><p>Your child must first complete the Bronze Award. We will then contact you with the next dates.</p></div>
      <div class="faq-item"><h3>Will I meet a Valemark player?</h3><p>Yes. Whilst on the programme you will have a chance to meet and learn from our players.</p></div>
      <div class="faq-item"><h3>How do you comply with safeguarding?</h3><p>This is really important to us. All coaches are trained in safeguarding and first aid and are DBS checked.</p></div>
    </section>
    <section class="mission" role="img" aria-label="Photo of a rugby pitch">
      <h2>Our Mission</h2>
      <p>To educate, inspire, mentor and transfer key leadership skills to the next generation</p>
    </section>
    <section class="about">
      <h2>Valemark</h2>
      <p>Valemark Rugby is a club built on the belief that sport can shape character. It brings together players, coaches and families to create a proud and welcoming community both on and off the pitch.</p>
      <p>Our coaches have played at every level of the game and share what they have learned with the next generation, helping young people grow in confidence, teamwork and leadership.</p>
      <p class="contact">Get in touch: www.valemark-rss.com &nbsp;·&nbsp; maris@valemark-rss.com</p>
    </section>
  </article>

</main>
</body>
</html>
```